Skyscraper (160x600), Banner (728x90), Banner (300x250)
Zielgruppe
Frauen zwischen 20 und 40 mit Kinderwunsch, die es auf emotionaler Ebene anzusprechen gilt
Aufgabenstellung
Wir suchen ansprechend kreativ gestaltete Werbemittel für unseren Ovulationstest FertaLINE. Dies ist ein Urin-Schnelltest, mit dem Frauen, die schwanger werden wollen, ihre fruchtbaren Tage bestimmen können. Er funktioniert genauso wie ein Schwangerschaftstest. Die Ansprache soll sehr emotional gestaltet werden, da ein hoch emotionales Thema

```html
<!DOCTYPE html>
<html lang="de">
<head>
<meta charset="utf-8">
<title>FertaLINE Werbebanner</title>
<link rel="stylesheet" href="https://fonts.googleapis.com/css2?family=Tinos:wght@700&display=swap">
<style>
  :root {
    --board: #e9eaeb;
    --banner-bg: #ffffff;
    --rose: #c77d95;
    --teal: #5b8ea9;
    --ink: #1a1a1a;
    --skin-light: #f3e6e0;
    --skin-mid: #d9b9ab;
    --mist-light: #e6edf3;
    --mist-mid: #a9bccb;
    --box-light: #eef4f8;
    --box-mid: #9fc3da;
    --shadow: rgba(0, 0, 0, 0.28);
  }
  * { margin: 0; padding: 0; box-sizing: border-box; }
  html, body {
    width: 1200px;
    height: 636px;
    overflow: hidden;
    background: var(--board);
  }
  .board { position: relative; width: 1200px; height: 636px; }
  .banner {
    position: absolute;
    left: 52px;
    width: 1098px;
    height: 138px;
    background: var(--banner-bg);
    box-shadow: 0 6px 8px var(--shadow);
    overflow: hidden;
    font-family: "Tinos", "Times New Roman", serif;
    font-weight: 700;
  }
  .banner--teaser { top: 117px; }
  .banner--offer { top: 333px; }

  .photo { position: absolute; top: 0; height: 100%; }
  .photo--hands {
    left: 0; width: 255px;
    background: linear-gradient(90deg, var(--skin-mid) 0%, var(--skin-light) 55%, var(--banner-bg) 100%);
  }
  .photo--baby-face {
    right: 0; width: 380px;
    background: linear-gradient(90deg, var(--banner-bg) 0%, var(--mist-light) 25%, var(--mist-mid) 100%);
    clip-path: polygon(10% 0, 100% 0, 100% 100%, 0 100%);
  }
  .teaser-headline {
    position: absolute;
    left: 288px; top: 22px;
    color: var(--rose);
    font-size: 45px;
    line-height: 55px;
  }

  .photo--sleeping-baby {
    left: 0; width: 225px;
    background: linear-gradient(90deg, var(--mist-mid) 0%, var(--mist-light) 60%, var(--banner-bg) 100%);
  }
  .photo--product {
    right: 0; width: 206px;
    background: linear-gradient(160deg, var(--box-light) 0%, var(--box-mid) 55%, var(--box-light) 100%);
  }
  .offer-copy {
    position: absolute;
    left: 277px; width: 668px; top: 18px;
    text-align: center;
  }
  .offer-headline {
    color: var(--teal);
    font-size: 26px;
    line-height: 35px;
  }
  .order-link {
    display: inline-block;
    margin-top: 13px;
    color: var(--ink);
    font-size: 19px;
    text-decoration: underline;
  }
</style>
</head>
<body>
<main class="board">
  <section class="banner banner--teaser">
    <div class="photo photo--hands" role="img" aria-label="Babyfüße in der Hand eines Erwachsenen"></div>
    <h1 class="teaser-headline">Wenn Träume auf<br>sich warten lassen ...</h1>
    <div class="photo photo--baby-face" role="img" aria-label="Nahaufnahme eines Babys in kühlen Blautönen"></div>
  </section>

  <section class="banner banner--offer">
    <div class="photo photo--sleeping-baby" role="img" aria-label="Schlafendes Baby in hellen Blautönen"></div>
    <div class="offer-copy">
      <h2 class="offer-headline">Ermitteln Sie Ihre fruchtbarsten Tage schnell<br>und zuverlässig mit dem Eisprungtest FertaLINE</h2>
      <a class="order-link" href="#">Hier bestellen</a>
    </div>
    <div class="photo photo--product" role="img" aria-label="Produktverpackung des Eisprungtests FertaLINE mit Teststreifen"></div>
  </section>
</main>
</body>
</html>
```